Quorlify Business Card

We require a stunning business card for Quorlify - a new digital marketing agency. The logo provided was designed by a graphic designer here on Artboxly.

www.quorlify-example.com - "Get more sales online"

What we do:
The business delivers website optimisation (Web design, social media strategy, digital strategies, SEO, PPC, conversion optimisation, email marketing) to get businesses more sales online.

The card must match the brand style which can be found on this website template:

http://layoutmarket.example/item/brightline-adaptive-versatile-layout/full_screen_preview/9137462

It must have 'wow' factor so that you'll never forget Quorlify - We're open to any materials, textures you think will work.

We don't want a boring run of the mill design - I can knock that up in Photoshop myself or use a template solution. It should be timeless and only need replacing should the contact details change.

The design should be eye catching, future proof, exceptionally chic, classy and oozing authority and confidence. Quorlify services must not look cheap.

Here's some brilliant designs to point you in the right direction:

http://tidyprints.example/30-remarkable-calling-cards/

The spec is for double sided, but we're open to your ideas. If it's going on an opaque or see through card, then of course a single side is preferable. Using creativity and thought on the medium for the card - shape - texture is desirable.

The strapline for the business is "Get more business online" please submit with / without strapline.
Updates

Please only submit your best 1-3 designs initially.

Target Market(s)

Business 2 Business - Local SMEs
Local professionals - Doctors, Dentists, Financials, Bespoke Retailers, Property companies - anyone with a decent budget to spend on digital marketing services and a high margin product or service to sell.

Industry/Entity Type

Graphic Designer

Requirements
Must have
• Text:
• name: Tom Vandlow
• position Digital Marketing Director
• mobile 07951 238 604
• website www.quorlify-example.com
Nice to have
• Check See http://tidyprints.example/30-remarkable-calling-cards/ for ideas.
• LinkedIn and Twitter usernames if there is space and it works on the design.

```html
<!DOCTYPE html>
<html lang="en">
<head>
<meta charset="utf-8">
<title>Quorlify Business Card</title>
<link rel="stylesheet" href="https://fonts.googleapis.com/css2?family=Jost:wght@400;500;600&display=swap">
<style>
  :root {
    --navy: #0b3552;
    --red: #e8201a;
    --paper: #f6f8f8;
    --stage: #141618;
    --muted: #c9d6df;
    --white: #ffffff;
  }
  * { box-sizing: border-box; margin: 0; padding: 0; }
  html, body {
    width: 1200px; height: 1000px; overflow: hidden;
    background: var(--stage);
    font-family: "Jost", "Futura", sans-serif;
  }
  .canvas {
    width: 1200px; height: 1000px;
    display: flex; flex-direction: column; align-items: center; justify-content: center;
    gap: 44px;
  }
  .card {
    width: 700px; height: 400px;
    background: var(--paper);
    position: relative; overflow: hidden;
    box-shadow: 0 14px 30px rgba(0,0,0,.45);
  }
  /* Front */
  .brand {
    position: absolute; left: 70px; top: 135px;
    display: flex; align-items: center; gap: 18px;
  }
  .brand-dot {
    width: 52px; height: 52px; border-radius: 50%;
    background: var(--red);
  }
  .brand-name {
    font-size: 84px; font-weight: 500; line-height: 1;
    color: var(--navy); letter-spacing: -1px;
  }
  .strapline {
    position: absolute; left: 142px; top: 240px;
    font-size: 18px; font-weight: 600; color: var(--navy);
  }
  /* Back */
  .card-back { display: flex; }
  .back-identity { flex: 0 0 56%; position: relative; }
  .person { position: absolute; left: 70px; top: 84px; }
  .person-name {
    font-size: 24px; font-weight: 600; color: var(--navy);
    display: flex; align-items: center; gap: 12px;
  }
  .person-name::before {
    content: ""; width: 11px; height: 11px; border-radius: 50%;
    background: var(--red);
  }
  .person-role {
    font-size: 18px; font-weight: 400; color: var(--navy);
    margin: 2px 0 0 60px; white-space: nowrap;
  }
  .back-contact { flex: 1; background: var(--navy); position: relative; }
  .contact-list {
    position: absolute; left: 40px; top: 190px;
    list-style: none; color: var(--muted); font-size: 15px; line-height: 1.6;
    white-space: nowrap;
  }
  .contact-list::before {
    content: ""; display: block; width: 11px; height: 11px; border-radius: 50%;
    background: var(--white); margin: 0 0 4px -22px;
  }
  .contact-list b { color: var(--white); font-weight: 500; font-size: 17px; margin-right: 5px; }
</style>
</head>
<body>
<main class="canvas">
  <section class="card card-front" aria-label="Card front">
    <div class="brand">
      <span class="brand-dot"></span>
      <span class="brand-name">Quorlify</span>
    </div>
    <p class="strapline">Get more business online</p>
  </section>

  <section class="card card-back" aria-label="Card back">
    <div class="back-identity">
      <div class="person">
        <p class="person-name">Tom Vandlow</p>
        <p class="person-role">Digital Marketing Director</p>
      </div>
    </div>
    <div class="back-contact">
      <ul class="contact-list">
        <li><b>Tel.</b>07951 238 604</li>
        <li><b>E</b>tom.vandlow@quorlify-example.com</li>
        <li><b>W</b>www.quorlify-example.com</li>
        <li><b>tw</b>@quorlify</li>
        <li><b>in</b>www.netprofile.example/quorlify</li>
      </ul>
    </div>
  </section>
</main>
</body>
</html>
```